Package design for paper cups, bags and a sweets box (white or grey color)
I have logo designed.
name of brand (MORVELLA)

Requirements
Should not have
• The color must be gray or white, and yellow and blue can be used

```html
<!DOCTYPE html>
<html lang="en">
<head>
<meta charset="utf-8">
<title>Morvella Specialty Coffee – Bag Label</title>
<link rel="stylesheet" href="https://fonts.googleapis.com/css2?family=Montserrat:wght@500;700&display=swap">
<style>
  :root {
    --paper: #f7f7f6;
    --ink: #1e1e1e;
    --petal-deep: #f5a544;
    --petal-light: #f6d08f;
  }
  html, body {
    margin: 0;
    padding: 0;
    width: 1200px;
    height: 1000px;
    overflow: hidden;
    background: var(--paper);
  }
  .label {
    position: relative;
    width: 1200px;
    height: 1000px;
  }
  .petal-ring {
    position: absolute;
    left: 0;
    top: 0;
    width: 1200px;
    height: 1000px;
  }
  .brand-lockup {
    position: absolute;
    left: 50%;
    top: 500px;
    transform: translate(-50%, -50%);
    display: flex;
    flex-direction: column;
    align-items: center;
    font-family: "Montserrat", sans-serif;
    color: var(--ink);
  }
  .brand-mark {
    width: 92px;
    height: 92px;
    border: 5px solid var(--ink);
    border-radius: 50%;
    box-sizing: border-box;
    margin-bottom: 18px;
  }
  .brand-name {
    font-weight: 700;
    font-size: 46px;
    letter-spacing: 0.16em;
    line-height: 1;
    margin-right: -0.16em;
  }
  .brand-tagline {
    font-weight: 700;
    font-size: 15px;
    letter-spacing: 0.14em;
    margin-top: 8px;
    margin-right: -0.14em;
  }
</style>
</head>
<body>
  <main class="label">
    <svg class="petal-ring" viewBox="0 0 1200 1000" role="img" aria-label="Ring of orange and pale yellow sunflower-like petals around the brand name">
      <defs>
        <radialGradient id="petal-tone" cx="600" cy="500" r="330" gradientUnits="userSpaceOnUse">
          <stop offset="0.45" stop-color="var(--petal-light)"/>
          <stop offset="0.75" stop-color="var(--petal-deep)"/>
          <stop offset="1" stop-color="var(--petal-light)"/>
        </radialGradient>
      </defs>
      <circle cx="600" cy="500" r="240" fill="none" stroke="url(#petal-tone)" stroke-width="180"/>
    </svg>

    <div class="brand-lockup">
      <div class="brand-mark"></div>
      <div class="brand-name">MORVELLA</div>
      <div class="brand-tagline">SPECIALTY COFFEE</div>
    </div>
  </main>
</body>
</html>
```